I already have a logo created by Sketch Harbor that I'm very happy with. I need to spruce up my business card now. Its a double sided card with not much info on it, I like to keep it simple.
Front of card: name, phone # email address, web address. Tag Line "Outsourced Technology Solutions", under that it says Business Voice Services & Electronic Protection.
Rear of Card: Content written inside a "cloud" saying "Cloud Solutions" "Cloud Integrity"

Target Market(s)

Business to Business

Industry/Entity Type

Business

Contact Information for Business Card

We are in the technology field. Providing Telephone systems (hardware), SIP Trunks (dial tone/local/long distance/telephone #'s), LAN (Local Area Network)infrastructure cabling, Data Center solutions and Security Applications (Camera systems, Access Control systems,

Requirements
Must have
• Must have brevity
Should not have
• Clutter and/or too much information

```html
<!DOCTYPE html>
<html lang="en">
<head>
<meta charset="utf-8">
<title>Northvale Signal Systems – Business Card</title>
<link rel="stylesheet" href="https://fonts.googleapis.com/css2?family=Montserrat:wght@700&family=Open+Sans:wght@400;600;700&family=Libre+Baskerville:wght@700&family=Arvo:wght@700&display=swap">
<style>
  :root {
    --page: #e9e6e1;
    --navy: #0f1a2a;
    --navy-deep: #0a121f;
    --band-blue: #3c68a6;
    --brand-blue: #24468f;
    --orange: #ee7a45;
    --ink: #1b2a44;
    --white: #ffffff;
    --cloud-a: #2f63b8;
    --cloud-b: #15356e;
  }
  * { box-sizing: border-box; margin: 0; padding: 0; }
  html, body { width: 1200px; height: 799px; overflow: hidden; }
  body {
    background: var(--page);
    display: flex;
    flex-direction: column;
    align-items: center;
    justify-content: center;
    gap: 28px;
  }
  .card {
    position: relative;
    width: 640px;
    height: 366px;
    overflow: hidden;
    box-shadow: 0 6px 18px rgba(0,0,0,.18);
  }

  /* Rear side */
  .card--rear {
    background: radial-gradient(ellipse at 50% 50%, #13243b 0%, var(--navy-deep) 75%);
  }
  .rear-brand {
    position: absolute;
    left: 26px; top: 24px;
    display: flex; align-items: center; gap: 8px;
    font: 700 11px "Montserrat", sans-serif;
    color: var(--band-blue);
  }
  .rear-brand .mark { width: 12px; height: 12px; background: var(--band-blue); }
  .cloud-art {
    position: absolute;
    left: 150px; top: 70px;
    width: 340px; height: 230px;
  }
  .cloud-copy {
    position: absolute;
    left: 0; right: 0; top: 150px;
    text-align: center;
    color: var(--white);
    font-family: "Open Sans", sans-serif;
    font-weight: 700;
    text-shadow: 0 0 8px rgba(120,170,255,.8);
  }
  .cloud-copy .title { font-size: 34px; letter-spacing: 1px; line-height: 1.1; }
  .cloud-copy .subtitle { font-size: 18px; letter-spacing: 1px; margin-left: 90px; }

  /* Front side */
  .card--front { background: var(--white); }
  .front-brand {
    position: absolute;
    left: 0; right: 0; top: 52px;
    display: flex; justify-content: center; align-items: center; gap: 10px;
    font: 700 23px "Montserrat", sans-serif;
    color: var(--brand-blue);
  }
  .front-brand .mark { width: 20px; height: 20px; background: var(--brand-blue); }
  .tagline-band {
    position: absolute;
    left: 0; top: 196px; width: 640px; height: 44px;
    background: var(--band-blue);
    padding-left: 22px;
    display: flex; align-items: center;
    font: 400 20px "Open Sans", sans-serif;
    color: var(--ink);
  }
  .contact-block {
    position: absolute;
    right: 0; top: 150px; width: 270px; height: 150px;
    background: var(--navy);
    clip-path: polygon(8% 0, 100% 0, 100% 100%, 0 100%, 0 60%);
    padding: 18px 0 0 44px;
    color: var(--white);
    font: 600 12px "Open Sans", sans-serif;
  }
  .contact-block li {
    list-style: none;
    display: flex; align-items: center; gap: 8px;
    height: 22px;
  }
  .contact-block svg { width: 13px; height: 13px; flex: none; }
  .name-band {
    position: absolute;
    left: 0; top: 246px; width: 410px; height: 52px;
    background: var(--orange);
    clip-path: polygon(0 0, 96% 0, 100% 50%, 96% 100%, 0 100%);
    padding-left: 56px;
    display: flex; align-items: center;
    font: 700 31px "Libre Baskerville", serif;
    letter-spacing: 4px;
    color: #000;
  }
  .services-band {
    position: absolute;
    left: 0; bottom: 0; width: 640px; height: 60px;
    background: var(--navy);
    display: flex; align-items: center; justify-content: center;
    font: 700 17px "Arvo", serif;
    color: var(--white);
  }
  .services-band::before {
    content: "";
    position: absolute; left: 0; right: 0; top: -6px; height: 6px;
    background: var(--white);
  }
</style>
</head>
<body>

  <section class="card card--rear" aria-label="Card rear">
    <div class="rear-brand"><span class="mark"></span>Northvale Signal Systems</div>
    <svg class="cloud-art" viewBox="0 0 340 230" role="img" aria-label="Cloud shape filled with small technology icons">
      <defs>
        <linearGradient id="cloudFill" x1="0" y1="0" x2="0" y2="1">
          <stop offset="0" stop-color="var(--cloud-a)"/>
          <stop offset="1" stop-color="var(--cloud-b)"/>
        </linearGradient>
      </defs>
      <path fill="url(#cloudFill)" d="M60 200 C20 200 5 170 20 145 C10 115 40 95 65 105 C70 65 110 45 145 60 C165 20 235 20 250 70 C285 60 320 85 310 120 C338 135 335 195 290 200 Z"/>
    </svg>
    <div class="cloud-copy">
      <p class="title">Cloud Solution</p>
      <p class="subtitle">Cloud Integrity</p>
    </div>
  </section>

  <section class="card card--front" aria-label="Card front">
    <div class="front-brand"><span class="mark"></span>Northvale Signal Systems, LLC</div>

    <div class="tagline-band">Outsourced Technology Solutions</div>

    <ul class="contact-block">
      <li>
        <svg viewBox="0 0 16 16" fill="none" stroke="currentColor" stroke-width="1.5"><rect x="1.5" y="3.5" width="13" height="9"/><path d="M1.5 3.5l6.5 5 6.5-5"/></svg>
        : yourname@northvalesignal.com
      </li>
      <li>
        <svg viewBox="0 0 16 16" fill="currentColor"><path d="M3 1.5l3 3-1.5 1.8c.8 1.8 2.4 3.4 4.2 4.2L10.5 9l3 3-2 2C6.5 13.5 2.5 9.5 1 4.5z"/></svg>
        : 12345-678-90
      </li>
      <li>
        <svg viewBox="0 0 16 16" fill="none" stroke="currentColor" stroke-width="1.3"><circle cx="8" cy="8" r="6.5"/><ellipse cx="8" cy="8" rx="3" ry="6.5"/><path d="M1.5 8h13"/></svg>
        : www.northvalesignal.com
      </li>
    </ul>

    <div class="name-band">Your Name</div>

    <div class="services-band">Business Voice Services &amp; Electronic Protection</div>
  </section>

</body>
</html>
```